Restaurant menu design

I need a menu for a restaurant in Spain.
It has to be bohemian but modern. We need something romantic and elegant.
The restaurant is elegant with good food and an excellent reputation. It is also modern at the same time.
The restaurant is superbly decorated and very chick so we need something "class" to fit in with the surroundings.
The size of the document must be 325 mm in high and 245 mm as a maximum and preferably made in indesign.

Reason: Thank you all for your designs.
So far all your designs are ok but it isn´t what we are looking for. Most of the designs are too loaded, too many colors and too much decoration.

Target Market(s)

Adults of various age groups and different nationalities mostly European.

Industry/Entity Type

Restaurant

Requirements
Must have
• The menu must have two interior pages with the text as in the document attached.It must be easily legible.
Nice to have
• See what kind of menus they use in important restaurants in places like Paris, see what designs are in trend, but Not necessarily doing the same style if it doesn’t fit in with the description above.
Should not have
• Nothing old fashioned.

```html
<!DOCTYPE html>
<html lang="es">
<head>
<meta charset="utf-8">
<title>La Rêverie — Carta</title>
<link rel="stylesheet" href="https://fonts.googleapis.com/css2?family=EB+Garamond:ital,wght@0,400;0,500;1,400&display=swap">
<style>
  :root {
    --paper: #f6f0e4;
    --ink: #1d1a17;
    --wine: #8a1a22;
    --rose: #d197a3;
    --frame: #8c8681;
    --page-bg: #ffffff;
    --gutter: #e6ded0;
  }
  * { margin: 0; padding: 0; box-sizing: border-box; }
  html, body {
    width: 1200px; height: 900px; overflow: hidden;
    background: var(--page-bg);
    font-family: "EB Garamond", Garamond, serif;
    color: var(--ink);
  }
  .spread {
    position: absolute; left: 0; top: 53px;
    width: 1200px; height: 794px;
    background: var(--paper);
    border-top: 1px solid var(--frame);
    border-bottom: 1px solid var(--frame);
  }
  .wash {
    position: absolute; left: 0; top: 0; width: 120px; height: 100%;
    background: linear-gradient(180deg, #ece3d4 0%, #e9d6b7 22%, #e8c9a2 40%, #e0c2b4 60%, #dab2bf 78%, #d7a6bb 100%);
    border-right: 3px solid var(--rose);
  }
  .fold {
    position: absolute; left: 600px; top: 0; width: 1px; height: 100%;
    background: var(--gutter);
  }
  .edge-band {
    position: absolute; right: 0; top: 0; width: 27px; height: 100%;
    background: var(--rose);
    border-left: 1px solid #b97d8a;
  }
  .section { position: absolute; }
  .section h2 {
    font-weight: 400;
    font-variant: small-caps;
    font-size: 22px;
    letter-spacing: 1.2px;
    color: var(--wine);
    line-height: 1;
    margin-bottom: 14px;
  }
  .dishes { list-style: none; }
  .dishes li {
    display: flex; justify-content: space-between; align-items: baseline;
    font-size: 12.2px;
    height: 20.7px; line-height: 20.7px;
    white-space: nowrap;
  }
  .dishes em { font-style: italic; }
  .dishes .price { text-align: right; }
  .col-left { left: 187px; width: 341px; }
  .col-right { left: 663px; width: 466px; }
  .starters { top: 78px; }
  .grill { top: 408px; }
  .kids { top: 636px; }
  .meats { top: 78px; }
  .desserts { top: 490px; }
  .sauces {
    position: absolute; left: 663px; top: 416px;
    width: 466px; height: 35px;
    border: 1px solid var(--frame);
    display: flex; align-items: center; justify-content: center;
    font-size: 10.6px; white-space: nowrap;
  }
  .sauces .label {
    font-variant: small-caps; color: var(--wine);
    font-size: 15px; letter-spacing: 0.6px; margin-right: 4px;
  }
  .sauces .dot { margin: 0 5px; }
</style>
</head>
<body>
<div class="spread">
  <div class="wash" role="img" aria-label="Franja de acuarela en tonos crema, ocre y rosa"></div>
  <div class="fold"></div>
  <div class="edge-band"></div>

  <section class="section col-left starters">
    <h2>Entradas</h2>
    <ul class="dishes">
      <li><span>Ensalada La Rêverie. Lechuga, tomate.</span><span class="price">7,75 €</span></li>
      <li><span>Ensalada Caprese <em>(Tomate y Mozzarella)</em>.</span><span class="price">7,75 €</span></li>
      <li><span>Escarola al Queso de Cabra con Bacon.</span><span class="price">6,75 €</span></li>
      <li><span>Cocktail de Gambas, Langostinos y Aguacate.</span><span class="price">7,50 €</span></li>
      <li><span>La Sopa de Pescado.</span><span class="price">8,25 €</span></li>
      <li><span>Crema de Espárragos Trigueros y Calabacín.</span><span class="price">5,95 €</span></li>
      <li><span>Carpaccio de Ternera.</span><span class="price">11,50 €</span></li>
      <li><span>Carpaccio de Salmón al Eneldo.</span><span class="price">9,75 €</span></li>
      <li><span>Carpaccio de Atún.</span><span class="price">13,95 €</span></li>
      <li><span>Melón con Jamón Ibérico.</span><span class="price">9,25 €</span></li>
      <li><span>Parrillada de Verduras.</span><span class="price">7,95 €</span></li>
      <li><span>Parrillada de Verduras Gratinada al Queso de Cabra.</span><span class="price">8,95 €</span></li>
      <li><span>Gambas Roja de la Bahía.</span><span class="price">12,95 €</span></li>
    </ul>
  </section>

  <section class="section col-left grill">
    <h2>Pescados al Grill</h2>
    <ul class="dishes">
      <li><span>Lubina al Hinojo.</span><span class="price">15,50 €</span></li>
      <li><span>Lubina Fileteada y su Salsa Rústica con Berenjena.</span><span class="price">18,50 €</span></li>
      <li><span>Filete de Rodaballo y su Salsa de Marisco.</span><span class="price">17,25 €</span></li>
      <li><span>Dorada del Mediterráneo.</span><span class="price">13,95 €</span></li>
      <li><span>Lenguado al Grill con Hierbas Provenzales.</span><span class="price">20,75 €</span></li>
      <li><span>Pieza de Atún Fresco y su Salsa Griega.</span><span class="price">18,95 €</span></li>
      <li><span>Lomo de Salmón con Salsa de Frambuesa.</span><span class="price">11,25 €</span></li>
      <li><span>Parrillada &nbsp;de &nbsp;Pescado &nbsp;y Marisco.</span><span class="price">23,505 €</span></li>
    </ul>
  </section>

  <section class="section col-left kids">
    <h2>Especial Niños</h2>
    <ul class="dishes">
      <li><span>Solomillo Junior, huevo y patatas fritas.</span><span class="price">6,25 €</span></li>
      <li><span>Fish &amp; chips.</span><span class="price">6,25 €</span></li>
    </ul>
  </section>

  <section class="section col-right meats">
    <h2>Carnes</h2>
    <ul class="dishes">
      <li><span>Pechuga de Pollo “Marie Louise” con Champiñones y Bacon.</span><span class="price">11,95 €</span></li>
      <li><span>Chuletas de Cordero.</span><span class="price">14,50 €</span></li>
      <li><span>Costillas de Cerdo con Salsa Barbacoa.</span><span class="price">9,95 €</span></li>
      <li><span>Paletilla de Cordero Lechal.</span><span class="price">19,75 €</span></li>
      <li><span>Le Strogonoff. <em>Finas tiras de Solomillo con su Salsa de Champiñones.</em></span><span class="price">15,90 €</span></li>
      <li><span>Solomillo de Ternera.</span><span class="price">18,50 €</span></li>
      <li><span>Solomillo de Ternera a la Ibérica con Jamón Ibérico y Ligera Salsa de Vino Tinto.</span><span class="price">20,75 €</span></li>
      <li><span>“Burger Salon Steak Haché”.</span><span class="price"></span></li>
      <li><span><em>Picada de Solomillo de Ternera, Huevo Frito y Patatas Fritas</em></span><span class="price">14,50 €</span></li>
      <li><span>Solomillo de Cerdo al Horno con Bacon y su Salsa de Setas.</span><span class="price">14,25 €</span></li>
      <li><span>Entrecôte de &nbsp;Ternera.</span><span class="price">14,75 €</span></li>
      <li><span>T-Bone Steak de Ternera.</span><span class="price">16,75 €</span></li>
      <li><span>Chuletón de Ternera.</span><span class="price">20,25 €</span></li>
      <li><span>Parrillada de Carnes y Embutidos.</span><span class="price">21,50 €</span></li>
    </ul>
  </section>

  <div class="sauces">
    <span class="label">Salsas.</span>
    <span>Pimienta. 2,85 €</span><span class="dot">·</span>
    <span>Roquefort. 2,95 €</span><span class="dot">·</span>
    <span>Bearnaise. 2,95 €</span><span class="dot">·</span>
    <span>de Champiñones. 2,65 €</span>
  </div>

  <section class="section col-right desserts">
    <h2>Los Postres de la Rêverie</h2>
    <ul class="dishes">
      <li><span>Frambuesas “La Rêverie”.</span><span class="price">6,25 €</span></li>
      <li><span>Cocktail de Frutas Exóticas.</span><span class="price">5,25 €</span></li>
      <li><span>Sorbete de Limón, Coulis de Fresa y Vodka.</span><span class="price">5,50 €</span></li>
      <li><span>Pastel de Chocolate Casero con su Salsa de Vainilla.</span><span class="price">6,25 €</span></li>
      <li><span>Crème Brulée.</span><span class="price">6,25 €</span></li>
      <li><span>Tarta de Manzana Casera “Tatín” y su Helado de Vainilla.</span><span class="price">6,95 €</span></li>
      <li><span>Copa Glacier Nord.</span><span class="price">6,75 €</span></li>
      <li><span>Pera al Chocolate Caliente y Helado de Macadamia.</span><span class="price">5,95 €</span></li>
      <li><span>Tarta de Queso con Coulis de Fresa.</span><span class="price">5,75 €</span></li>
      <li><span>Nuestra Mousse de Chocolate.</span><span class="price">5,75 €</span></li>
    </ul>
  </section>
</div>
</body>
</html>
```